Ridgeline Trek Supply - Business Card Design Project

Our company is Ridgeline Trek Supply. We make outdoor gear such as headlamps and flashlights. If you would like to get a feel for our company, feel free to look at our website. www.ridgelinetreksupply.example

And here is my information to put on the card.
Ridgeline Trek Supply
Dana Whitlock
41596 Juniper Hollow Road
Cedar Bluff, WA. 97530
support@RidgelineTrekSupply.example
www.RidgelineTrekSupply.example
Facebook.com/RidgelineTrekSupply
Pinterest.com/RidgelineTrekSupply
Twitter.com/RidgelineTrekSupply

Target Market(s)

hunters, campers, preppers

Industry/Entity Type

Sporting Good

Contact Information for Business Card

We would like a card that looks a little outdoorsy. We have 2 logos so one of them should be on the card. The card should also use the colors that are on our logos. The name "Ridgeline Trek Supply" if written out should be in the font "Capture it".

Requirements
Must have
• We currently have 2 logos. At least one must be on the card.
• Must use colors from the logos.
Nice to have
• Possibly a quote from our website. Something like: We don’t just make outdoor gear. We use it. We know it. We live it and we love it.

```html
<!DOCTYPE html>
<html lang="en">
<head>
<meta charset="utf-8">
<title>Ridgeline Trek Supply – Business Cards</title>
<link href="https://fonts.googleapis.com/css2?family=Roboto:wght@400;500;700&family=Roboto+Condensed:ital,wght@0,700;1,700&display=swap" rel="stylesheet">
<style>
  :root {
    --bg: #e6e6e8;
    --brown-top: #6b5232;
    --brown-bottom: #3a2917;
    --brown-text: #3b2a1a;
    --gold: #c9a15a;
    --gold-dark: #a9803c;
    --white: #ffffff;
    --ink: #2e2418;
    --sky-blue: #3a9bd8;
    --pin-red: #d8332f;
    --face-blue: #3b6cb5;
  }
  * { box-sizing: border-box; margin: 0; padding: 0; }
  html, body { width: 1200px; height: 800px; overflow: hidden; }
  body {
    background: var(--bg);
    font-family: "Roboto", sans-serif;
    position: relative;
  }
  .card {
    position: absolute;
    top: 245px;
    width: 540px;
    height: 310px;
    border-radius: 4px;
    overflow: hidden;
    box-shadow: 0 6px 18px rgba(0,0,0,.15);
  }

  /* Front */
  .card-front {
    left: 40px;
    background: linear-gradient(180deg, var(--brown-top), var(--brown-bottom));
  }
  .forest {
    position: absolute;
    left: 0; right: 0; bottom: 0;
    height: 210px;
    background: linear-gradient(180deg, rgba(90,70,44,0) 0%, rgba(70,52,30,.55) 60%, rgba(50,36,20,.7) 100%);
  }
  .front-brand {
    position: absolute;
    top: 110px; left: 0; right: 0;
    text-align: center;
    font-family: "Roboto Condensed", sans-serif;
    font-weight: 700;
    font-size: 40px;
    color: var(--white);
    line-height: 1;
  }
  .social-row {
    position: absolute;
    top: 215px; left: 0; right: 0;
    display: flex;
    justify-content: center;
    align-items: center;
    gap: 8px;
    color: var(--white);
    font-size: 15px;
  }
  .social-dot {
    width: 18px; height: 18px;
    border-radius: 50%;
    border: 2px solid var(--white);
  }
  .social-dot.blue { background: var(--sky-blue); }
  .social-dot.red { background: var(--pin-red); }
  .social-dot.navy { background: var(--face-blue); }
  .social-handle { margin-left: 4px; }

  /* Back */
  .card-back {
    left: 620px;
    background: var(--white);
  }
  .back-brand {
    position: absolute;
    left: 26px; top: 74px;
    width: 190px;
    font-family: "Roboto Condensed", sans-serif;
    font-weight: 700;
    font-size: 30px;
    line-height: 1.05;
    color: var(--brown-text);
  }
  .divider {
    position: absolute;
    left: 232px; top: 60px;
    width: 1px; height: 120px;
    background: var(--brown-text);
  }
  .contact {
    position: absolute;
    left: 250px; top: 56px;
    right: 16px;
  }
  .contact-name {
    font-family: "Roboto Condensed", sans-serif;
    font-weight: 700;
    font-size: 22px;
    color: var(--brown-text);
    line-height: 1;
  }
  .contact-title {
    font-size: 9.5px;
    font-weight: 700;
    letter-spacing: .3px;
    color: var(--gold);
    margin: 3px 0 8px;
    text-transform: uppercase;
  }
  .contact-list { list-style: none; }
  .contact-list li {
    display: flex;
    align-items: flex-start;
    gap: 6px;
    font-size: 10.5px;
    color: var(--ink);
    line-height: 1.35;
    margin-bottom: 1px;
  }
  .contact-list svg { flex: none; width: 11px; height: 11px; margin-top: 2px; }
  .tagline {
    position: absolute;
    left: 26px; bottom: 48px;
  }
  .tagline-head {
    font-family: "Roboto Condensed", sans-serif;
    font-weight: 700;
    font-style: italic;
    font-size: 22px;
    color: var(--brown-text);
    line-height: 1;
  }
  .tagline-sub {
    font-size: 12px;
    font-weight: 500;
    color: var(--ink);
    margin-top: 4px;
  }
  .gold-band {
    position: absolute;
    left: 0; right: 0; bottom: 0;
    height: 22px;
    background: linear-gradient(90deg, var(--gold-dark), var(--gold));
  }
</style>
</head>
<body>

<section class="card card-front" aria-label="Business card front">
  <div class="forest" role="img" aria-label="Misty pine forest silhouette"></div>
  <div class="front-brand">Ridgeline Trek Supply</div>
  <div class="social-row">
    <span class="social-dot blue"></span>
    <span class="social-dot red"></span>
    <span class="social-dot navy"></span>
    <span class="social-handle">| RidgelineTrekSupply</span>
  </div>
</section>

<section class="card card-back" aria-label="Business card back">
  <div class="back-brand">Ridgeline Trek Supply</div>
  <div class="divider"></div>
  <div class="contact">
    <div class="contact-name">DANA WHITLOCK</div>
    <div class="contact-title">Founder &amp; Director of Operations</div>
    <ul class="contact-list">
      <li>
        <svg viewBox="0 0 12 12"><rect width="12" height="12" rx="2" fill="#3b2a1a"/><path d="M3.5 3c.6 2.6 2.4 4.6 5 5.5l.9-1-1.4-1-.7.6C6.3 6.5 5.5 5.7 5 4.7l.6-.7-1-1.4z" fill="#fff"/></svg>
        541-555-0148
      </li>
      <li>
        <svg viewBox="0 0 12 12"><rect width="12" height="12" rx="2" fill="#3b2a1a"/><rect x="2.5" y="3.5" width="7" height="5" fill="none" stroke="#fff"/><path d="M2.5 3.5 6 6.5 9.5 3.5" fill="none" stroke="#fff"/></svg>
        support@RidgelineTrekSupply.example
      </li>
      <li>
        <svg viewBox="0 0 12 12"><rect width="12" height="12" rx="2" fill="#3b2a1a"/><rect x="2.5" y="3" width="7" height="6" fill="none" stroke="#fff"/><line x1="2.5" y1="5" x2="9.5" y2="5" stroke="#fff"/></svg>
        www.RidgelineTrekSupply.example
      </li>
      <li>
        <svg viewBox="0 0 12 12"><path d="M6 1a3.2 3.2 0 0 0-3.2 3.2C2.8 6.6 6 11 6 11s3.2-4.4 3.2-6.8A3.2 3.2 0 0 0 6 1zm0 4.4a1.2 1.2 0 1 1 0-2.4 1.2 1.2 0 0 1 0 2.4z" fill="#3b2a1a"/></svg>
        <span>41596 Juniper Hollow Road<br>Cedar Bluff, WA. 97530</span>
      </li>
    </ul>
  </div>
  <div class="tagline">
    <div class="tagline-head">BUILT ON THE TRAIL, NOT THE SHELF.</div>
    <div class="tagline-sub">We test it, We trust it, We carry it and we stand by it.</div>
  </div>
  <div class="gold-band"></div>
</section>

</body>
</html>
```